Ridgeline Admin Crew needs a Ad design for products page

We need an Ad design on multiple formats for our website https://www.ridgelineadmincrew.example. Our products are mainly reports and guide for PFXQ and Velmora. We want to make sure people will see our products page easier with this ad banner. We would like to use kindly the same colors from our blog site. The Ad banner must be attractive, neutral colors and modern ad.

Target Market(s)

IT and Brantwick Products

Font styles to use
Other font styles liked:
• Google Font Lato

Colors
0792cd

Requirements
Must have
• We would like to use kindly the same colors from our blog site. The Ad banner must be attractive, neutral colors and modern ad.
Nice to have
• Nothing for the moment
Should not have
• Animation, no flashy

```html
<!DOCTYPE html>
<html lang="en">
<head>
<meta charset="utf-8">
<title>Ridgeline Admin Crew – Ad banner set</title>
<link href="https://fonts.googleapis.com/css2?family=Lato:wght@400;700;900&display=swap" rel="stylesheet">
<style>
  :root {
    --brand: #0792cd;
    --paper: #ffffff;
    --night: #061016;
    --deep: #0f2b38;
    --glow: #3fb8dc;
    --cta: #ff9900;
    --cta-text: #ffffff;
    --copy: #ffffff;
    --label: #222222;
  }
  html, body {
    margin: 0;
    padding: 0;
    width: 1200px;
    height: 1000px;
    overflow: hidden;
    background: var(--paper);
    font-family: "Lato", Arial, sans-serif;
  }
  .sheet { position: relative; width: 1200px; height: 1000px; }

  .banner { position: absolute; overflow: hidden; }
  .banner .backdrop { position: absolute; inset: 0; width: 100%; height: 100%; display: block; }

  .brand {
    position: absolute;
    display: flex;
    align-items: center;
    gap: 0.35em;
    color: var(--brand);
    font-weight: 400;
    white-space: nowrap;
    letter-spacing: -0.01em;
  }
  .brand .brand-dot {
    width: 1.6em; height: 1.6em;
    border-radius: 50%;
    background: var(--brand);
    flex: none;
  }

  .copy {
    position: absolute;
    left: 0; right: 0;
    text-align: center;
    color: var(--copy);
    line-height: 1.25;
  }
  .copy p { margin: 0; }
  .copy .question { font-weight: 400; }
  .copy .promise { text-transform: uppercase; font-weight: 400; }
  .copy .accent { color: var(--brand); font-weight: 700; }

  .cta {
    position: absolute;
    display: flex;
    align-items: center;
    justify-content: center;
    background: var(--cta);
    color: var(--cta-text);
    border-radius: 3px;
    text-transform: uppercase;
    font-weight: 400;
    white-space: nowrap;
  }
  .cta strong { font-weight: 900; margin-left: 0.3em; }

  .size-label {
    position: absolute;
    font-size: 14px;
    color: var(--label);
    text-align: right;
    width: 120px;
  }

  /* 320 x 100 */
  .b320 { left: 63px; top: 58px; width: 320px; height: 100px; }
  .b320 .brand { left: 6px; top: 5px; font-size: 8px; }
  .b320 .copy.q { top: 36px; font-size: 13px; }
  .b320 .copy.p { top: 57px; font-size: 12px; }
  .b320 .cta { left: 203px; top: 7px; width: 110px; height: 24px; font-size: 9px; }

  /* 200 x 200 */
  .b200 { left: 540px; top: 57px; width: 200px; height: 200px; }
  .b200 .brand { left: 0; right: 0; justify-content: center; top: 12px; font-size: 11px; }
  .b200 .copy.q { top: 78px; font-size: 12px; }
  .b200 .copy.p { top: 105px; font-size: 12px; }
  .b200 .cta { left: 23px; top: 156px; width: 153px; height: 33px; font-size: 12px; }

  /* 300 x 600 */
  .b600 { left: 855px; top: 58px; width: 300px; height: 600px; }
  .b600 .brand { left: 0; right: 0; justify-content: center; top: 28px; font-size: 19px; }
  .b600 .copy.q { top: 153px; font-size: 29px; line-height: 1.4; }
  .b600 .copy.p { top: 276px; font-size: 26px; line-height: 1.4; }
  .b600 .cta { left: 36px; top: 485px; width: 230px; height: 53px; font-size: 18px; }

  /* 300 x 250 */
  .b300 { left: 58px; top: 290px; width: 300px; height: 250px; }
  .b300 .brand { left: 0; right: 0; justify-content: center; top: 18px; font-size: 16px; }
  .b300 .copy.q { top: 95px; font-size: 17px; }
  .b300 .copy.p { top: 132px; font-size: 15px; }
  .b300 .cta { left: 61px; top: 195px; width: 177px; height: 40px; font-size: 15px; }

  /* 250 x 250 */
  .b250 { left: 515px; top: 355px; width: 250px; height: 250px; }
  .b250 .brand { left: 0; right: 0; justify-content: center; top: 18px; font-size: 13px; }
  .b250 .copy.q { top: 99px; font-size: 14px; }
  .b250 .copy.p { top: 133px; font-size: 14px; }
  .b250 .cta { left: 46px; top: 200px; width: 157px; height: 35px; font-size: 13px; }

  /* 336 x 280 */
  .b336 { left: 58px; top: 645px; width: 336px; height: 280px; }
  .b336 .brand { left: 0; right: 0; justify-content: center; top: 22px; font-size: 18px; }
  .b336 .copy.q { top: 106px; font-size: 19px; }
  .b336 .copy.p { top: 148px; font-size: 17px; line-height: 1.4; }
  .b336 .cta { left: 61px; top: 218px; width: 211px; height: 47px; font-size: 17px; }

  /* 468 x 60 */
  .b468 { left: 687px; top: 725px; width: 468px; height: 60px; }
  .b468 .brand { left: 4px; top: 24px; font-size: 9px; }
  .b468 .copy { left: 130px; right: 120px; font-size: 11px; line-height: 1.3; top: 9px; }
  .b468 .cta { left: 357px; top: 20px; width: 105px; height: 24px; font-size: 8px; }

  /* 728 x 90 */
  .b728 { left: 427px; top: 837px; width: 728px; height: 90px; }
  .b728 .brand { left: 8px; top: 36px; font-size: 13px; }
  .b728 .copy { left: 230px; right: 180px; top: 13px; font-size: 16px; line-height: 1.3; }
  .b728 .copy .promise { font-size: 15px; }
  .b728 .cta { left: 561px; top: 28px; width: 158px; height: 36px; font-size: 13px; }
</style>
</head>
<body>
<div class="sheet">

  <!-- 320 x 100 -->
  <div class="banner b320">
    <svg class="backdrop" viewBox="0 0 320 100" preserveAspectRatio="none" role="img" aria-label="Dark blue abstract network background with soft light glow">
      <defs>
        <radialGradient id="g320" cx="0.9" cy="0.6" r="0.7">
          <stop offset="0" stop-color="var(--glow)"/><stop offset="0.35" stop-color="var(--deep)"/><stop offset="1" stop-color="var(--night)"/>
        </radialGradient>
      </defs>
      <rect width="320" height="100" fill="url(#g320)"/>
      <path d="M0 0 H190 Q120 20 0 24 Z" fill="var(--paper)"/>
    </svg>
    <div class="brand"><span class="brand-dot"></span>Ridgeline Admin Crew</div>
    <div class="copy q"><p class="question">Need the best <span class="accent">PFXQ</span> solutions?</p></div>
    <div class="copy p"><p class="promise">Our experienced team<br>is <span class="accent">ready</span> to meet your needs</p></div>
    <div class="cta">Get<strong>my solution!</strong></div>
  </div>
  <div class="size-label" style="left:258px; top:170px;">320 x 100 px</div>

  <!-- 200 x 200 -->
  <div class="banner b200">
    <svg class="backdrop" viewBox="0 0 200 200" preserveAspectRatio="none" role="img" aria-label="Dark blue abstract network background with soft light glow">
      <defs>
        <radialGradient id="g200" cx="0.95" cy="0.45" r="0.8">
          <stop offset="0" stop-color="var(--glow)"/><stop offset="0.35" stop-color="var(--deep)"/><stop offset="1" stop-color="var(--night)"/>
        </radialGradient>
      </defs>
      <rect width="200" height="200" fill="url(#g200)"/>
      <path d="M0 0 H200 V40 Q100 56 0 40 Z" fill="var(--paper)"/>
    </svg>
    <div class="brand"><span class="brand-dot"></span>Ridgeline Admin Crew</div>
    <div class="copy q"><p class="question">Need the best <span class="accent">PFXQ</span> solutions?</p></div>
    <div class="copy p"><p class="promise">Our experienced team<br>is <span class="accent">ready</span> to meet your needs</p></div>
    <div class="cta">Get<strong>my solution!</strong></div>
  </div>
  <div class="size-label" style="left:622px; top:263px;">200 x 200 px</div>

  <!-- 300 x 600 -->
  <div class="banner b600">
    <svg class="backdrop" viewBox="0 0 300 600" preserveAspectRatio="none" role="img" aria-label="Dark blue abstract network background with soft light glow">
      <defs>
        <radialGradient id="g600" cx="1" cy="0.45" r="0.6">
          <stop offset="0" stop-color="var(--glow)"/><stop offset="0.35" stop-color="var(--deep)"/><stop offset="1" stop-color="var(--night)"/>
        </radialGradient>
      </defs>
      <rect width="300" height="600" fill="url(#g600)"/>
      <path d="M0 0 H300 V76 Q150 118 0 76 Z" fill="var(--paper)"/>
    </svg>
    <div class="brand"><span class="brand-dot"></span>Ridgeline Admin Crew</div>
    <div class="copy q"><p class="question">Need the best<br><span class="accent">PFXQ</span> solutions?</p></div>
    <div class="copy p"><p class="promise">Our<br>experienced team<br>is <span class="accent">ready</span> to<br>meet your needs</p></div>
    <div class="cta">Get<strong>my solution!</strong></div>
  </div>
  <div class="size-label" style="left:1035px; top:667px;">300 x 600 px</div>

  <!-- 300 x 250 -->
  <div class="banner b300">
    <svg class="backdrop" viewBox="0 0 300 250" preserveAspectRatio="none" role="img" aria-label="Dark blue abstract network background with soft light glow">
      <defs>
        <radialGradient id="g300" cx="1" cy="0.55" r="0.7">
          <stop offset="0" stop-color="var(--glow)"/><stop offset="0.35" stop-color="var(--deep)"/><stop offset="1" stop-color="var(--night)"/>
        </radialGradient>
      </defs>
      <rect width="300" height="250" fill="url(#g300)"/>
      <path d="M0 0 H300 V46 Q150 74 0 46 Z" fill="var(--paper)"/>
    </svg>
    <div class="brand"><span class="brand-dot"></span>Ridgeline Admin Crew</div>
    <div class="copy q"><p class="question">Need the best <span class="accent">PFXQ</span> solutions?</p></div>
    <div class="copy p"><p class="promise">Our experienced team<br>is <span class="accent">ready</span> to meet your needs</p></div>
    <div class="cta">Get<strong>my solution!</strong></div>
  </div>
  <div class="size-label" style="left:236px; top:545px;">300 x 250 px</div>

  <!-- 250 x 250 -->
  <div class="banner b250">
    <svg class="backdrop" viewBox="0 0 250 250" preserveAspectRatio="none" role="img" aria-label="Dark blue abstract network background with soft light glow">
      <defs>
        <radialGradient id="g250" cx="1" cy="0.5" r="0.7">
          <stop offset="0" stop-color="var(--glow)"/><stop offset="0.35" stop-color="var(--deep)"/><stop offset="1" stop-color="var(--night)"/>
        </radialGradient>
      </defs>
      <rect width="250" height="250" fill="url(#g250)"/>
      <path d="M0 0 H250 V44 Q125 68 0 44 Z" fill="var(--paper)"/>
    </svg>
    <div class="brand"><span class="brand-dot"></span>Ridgeline Admin Crew</div>
    <div class="copy q"><p class="question">Need the best <span class="accent">PFXQ</span> solutions?</p></div>
    <div class="copy p"><p class="promise">Our experienced team<br>is <span class="accent">ready</span> to meet your needs</p></div>
    <div class="cta">Get<strong>my solution!</strong></div>
  </div>
  <div class="size-label" style="left:645px; top:614px;">250 x 250 px</div>

  <!-- 336 x 280 -->
  <div class="banner b336">
    <svg class="backdrop" viewBox="0 0 336 280" preserveAspectRatio="none" role="img" aria-label="Dark blue abstract network background with soft light glow">
      <defs>
        <radialGradient id="g336" cx="1" cy="0.5" r="0.7">
          <stop offset="0" stop-color="var(--glow)"/><stop offset="0.35" stop-color="var(--deep)"/><stop offset="1" stop-color="var(--night)"/>
        </radialGradient>
      </defs>
      <rect width="336" height="280" fill="url(#g336)"/>
      <path d="M0 0 H336 V54 Q168 88 0 54 Z" fill="var(--paper)"/>
    </svg>
    <div class="brand"><span class="brand-dot"></span>Ridgeline Admin Crew</div>
    <div class="copy q"><p class="question">Need the best <span class="accent">PFXQ</span> solutions?</p></div>
    <div class="copy p"><p class="promise">Our experienced team<br>is <span class="accent">ready</span> to meet your needs</p></div>
    <div class="cta">Get<strong>my solution!</strong></div>
  </div>
  <div class="size-label" style="left:271px; top:934px;">336 x 280 px</div>

  <!-- 468 x 60 -->
  <div class="banner b468">
    <svg class="backdrop" viewBox="0 0 468 60" preserveAspectRatio="none" role="img" aria-label="Dark blue abstract network background with soft light glow">
      <defs>
        <radialGradient id="g468" cx="0.75" cy="0.5" r="0.5">
          <stop offset="0" stop-color="var(--glow)"/><stop offset="0.4" stop-color="var(--deep)"/><stop offset="1" stop-color="var(--night)"/>
        </radialGradient>
      </defs>
      <rect width="468" height="60" fill="url(#g468)"/>
      <path d="M0 0 H118 Q132 30 126 60 H0 Z" fill="var(--paper)"/>
    </svg>
    <div class="brand"><span class="brand-dot"></span>Ridgeline Admin Crew</div>
    <div class="copy"><p class="question">Need the best <span class="accent">PFXQ</span> solutions?</p><p class="promise">Our experienced team<br>is <span class="accent">ready</span> to meet your needs</p></div>
    <div class="cta">Get<strong>my solution!</strong></div>
  </div>
  <div class="size-label" style="left:1030px; top:790px;">468 x 60 px</div>

  <!-- 728 x 90 -->
  <div class="banner b728">
    <svg class="backdrop" viewBox="0 0 728 90" preserveAspectRatio="none" role="img" aria-label="Dark blue abstract network background with soft light glow">
      <defs>
        <radialGradient id="g728" cx="0.8" cy="0.5" r="0.4">
          <stop offset="0" stop-color="var(--glow)"/><stop offset="0.4" stop-color="var(--deep)"/><stop offset="1" stop-color="var(--night)"/>
        </radialGradient>
      </defs>
      <rect width="728" height="90" fill="url(#g728)"/>
      <path d="M0 0 H205 Q228 45 222 90 H0 Z" fill="var(--paper)"/>
    </svg>
    <div class="brand"><span class="brand-dot"></span>Ridgeline Admin Crew</div>
    <div class="copy"><p class="question">Need the best <span class="accent">PFXQ</span> solutions?</p><p class="promise">Our experienced team<br>is <span class="accent">ready</span> to meet your needs</p></div>
    <div class="cta">Get<strong>my solution!</strong></div>
  </div>
  <div class="size-label" style="left:1030px; top:933px;">728 x 90 px</div>

</div>
</body>
</html>
```